Cybersecurity company is looking for business card.

I need a business card design for our company, we are a cybersecurity company providing advance technology to protect agains any kind of malware. We need a fresh modern design it should communicate modern, technology and growth.

Target Market(s)

Business to business

Industry/Entity Type

Business

Contact Information for Business Card

Should have location, address, fax, mobile, phone, email and website.

Requirements
Must have
• Must follow company's logo color and style. Must have the company's log on its.

```html
<!DOCTYPE html>
<html lang="en">
<head>
<meta charset="utf-8">
<title>Kelvara Cybersecurity – Business Card</title>
<link rel="stylesheet" href="https://fonts.googleapis.com/css2?family=Open+Sans:wght@400;600;700;800&display=swap">
<style>
  :root {
    --backdrop: #cfe9e1;
    --carbon: #2a2a2d;
    --carbon-light: #343438;
    --crimson-deep: #8c1813;
    --crimson: #a83a2a;
    --crimson-soft: #c0684f;
    --paper: #ffffff;
    --ink: #111111;
    --text-light: #ffffff;
  }
  html, body {
    margin: 0;
    padding: 0;
    width: 1200px;
    height: 900px;
    overflow: hidden;
    background: var(--backdrop);
    font-family: "Open Sans", Arial, sans-serif;
  }
  .canvas {
    position: relative;
    width: 1200px;
    height: 900px;
  }
  .card {
    position: absolute;
    width: 560px;
    height: 320px;
    border-radius: 26px;
    overflow: hidden;
    box-shadow: 0 14px 30px rgba(40, 80, 70, 0.22);
  }
  .card svg.card-art {
    position: absolute;
    inset: 0;
  }
  .card-back { left: 560px; top: 110px; }
  .card-front { left: 80px; top: 450px; }

  .wordmark {
    position: absolute;
    font-weight: 800;
    letter-spacing: 1px;
    color: var(--ink);
    display: flex;
    align-items: center;
    gap: 8px;
    line-height: 1;
  }
  .wordmark .mark-dot {
    width: 10px;
    height: 10px;
    background: var(--crimson-deep);
  }
  .card-back .wordmark { left: 70px; top: 150px; font-size: 46px; }
  .card-front .wordmark { left: 300px; top: 110px; font-size: 44px; }

  .identity {
    position: absolute;
    left: 64px;
    top: 92px;
    color: var(--text-light);
  }
  .identity .company {
    font-size: 24px;
    font-weight: 800;
    letter-spacing: 0.5px;
    line-height: 1;
  }
  .identity .tagline {
    font-size: 13px;
    margin-top: 1px;
    padding-left: 14px;
  }
  .identity .tagline strong { font-weight: 700; }

  .contact {
    position: absolute;
    left: 64px;
    top: 160px;
    color: var(--text-light);
    font-size: 11.5px;
    line-height: 1.45;
  }
  .contact .address-line { font-weight: 600; }
  .contact .address-line.secondary { font-weight: 400; }
  .contact-list {
    list-style: none;
    margin: 4px 0 0;
    padding: 0;
  }
  .contact-list li {
    display: flex;
    align-items: center;
    gap: 12px;
    height: 16px;
  }
  .contact-list svg { width: 14px; height: 14px; flex: none; }
</style>
</head>
<body>
<main class="canvas">

  <!-- Card back -->
  <section class="card card-back" aria-label="Business card back">
    <svg class="card-art" viewBox="0 0 560 320" width="560" height="320" aria-hidden="true">
      <defs>
        <linearGradient id="backRed" x1="0" y1="0" x2="0.3" y2="1">
          <stop offset="0" stop-color="#8c1813"/>
          <stop offset="1" stop-color="#b25a46"/>
        </linearGradient>
        <linearGradient id="cornerRed" x1="0" y1="0" x2="1" y2="1">
          <stop offset="0" stop-color="#a63a29"/>
          <stop offset="1" stop-color="#c0684f"/>
        </linearGradient>
      </defs>
      <rect width="560" height="320" fill="url(#backRed)"/>
      <polygon points="310,320 470,0 560,0 560,120 460,320" fill="var(--carbon)"/>
      <polygon points="460,320 560,120 560,320" fill="url(#cornerRed)"/>
    </svg>
    <div class="wordmark"><span>kelvara</span><span class="mark-dot"></span></div>
  </section>

  <!-- Card front -->
  <section class="card card-front" aria-label="Business card front">
    <svg class="card-art" viewBox="0 0 560 320" width="560" height="320" aria-hidden="true">
      <defs>
        <linearGradient id="frontRed" x1="0" y1="0" x2="1" y2="1">
          <stop offset="0" stop-color="#c0684f"/>
          <stop offset="1" stop-color="#8c1813"/>
        </linearGradient>
      </defs>
      <rect width="560" height="320" fill="var(--carbon)"/>
      <polygon points="0,0 90,0 0,105" fill="url(#frontRed)"/>
      <polygon points="0,0 60,0 0,70" fill="var(--carbon)"/>
      <polygon points="0,105 90,0 120,0 0,140" fill="var(--carbon-light)"/>
      <polygon points="270,0 470,0 540,320 270,320" fill="var(--paper)"/>
      <polygon points="470,0 500,0 560,160 560,290 540,320 530,320" fill="url(#frontRed)"/>
      <polygon points="480,0 560,0 560,30" fill="var(--carbon)"/>
      <polygon points="215,320 270,245 270,320" fill="url(#frontRed)"/>
    </svg>

    <div class="identity">
      <div class="company">KELVARA</div>
      <div class="tagline">cyber<strong>security</strong></div>
    </div>

    <div class="contact">
      <div class="address-line">Harbor Tech Park (HTP)</div>
      <div class="address-line secondary">-Meridian Coast Road</div>
      <ul class="contact-list">
        <li>
          <svg viewBox="0 0 14 14" aria-label="Mobile"><rect x="3.5" y="0.8" width="7" height="12.4" rx="1.2" fill="none" stroke="#fff" stroke-width="1.2"/><circle cx="7" cy="11" r="0.7" fill="#fff"/></svg>
          <span>+971 50 000 0000</span>
        </li>
        <li>
          <svg viewBox="0 0 14 14" aria-label="Phone"><path d="M1 5 Q7 0 13 5 L11 7 L9 5.5 L5 5.5 L3 7 Z" fill="#fff"/><rect x="3" y="8" width="8" height="5" rx="1" fill="#fff"/></svg>
          <span>04 000 0000</span>
        </li>
        <li>
          <svg viewBox="0 0 14 14" aria-label="Fax"><rect x="3.5" y="1" width="7" height="4" fill="#fff"/><rect x="1" y="5.5" width="12" height="6" rx="1" fill="#fff"/><rect x="3.5" y="9" width="7" height="4" fill="#fff" stroke="#2a2a2d" stroke-width="0.8"/></svg>
          <span>000 . 0000 . 0000</span>
        </li>
        <li>
          <svg viewBox="0 0 14 14" aria-label="Email"><rect x="1" y="3" width="12" height="8" fill="#fff"/><path d="M1 3 L7 8 L13 3" fill="none" stroke="#2a2a2d" stroke-width="1"/></svg>
          <span>name.surname@kelvara.com</span>
        </li>
        <li>
          <svg viewBox="0 0 14 14" aria-label="Website"><rect x="1.5" y="2.5" width="11" height="8" rx="1" fill="none" stroke="#fff" stroke-width="1.2"/><rect x="4.5" y="11.5" width="5" height="1.2" fill="#fff"/></svg>
          <span>www.kelvara.com</span>
        </li>
      </ul>
    </div>

    <div class="wordmark"><span>kelvara</span><span class="mark-dot"></span></div>
  </section>

</main>
</body>
</html>
```